Stationary design for high end car detailer
Business card, letterheads, envelopes
Modern
Glanzwerk Garage
Tyttebærstien 7
0871 Oslo
post@glanzwerkstatt-eksempel.no
www.glanzwerkstatt-eksempel.no
We are looking for stationary designs to fit our new logo!
We are looking for something to match our high end profile
Primaily just the logo, but open for sugestions.

```html
<!DOCTYPE html>
<html lang="en">
<head>
<meta charset="utf-8">
<title>Glanzwerk Garage — Stationery</title>
<link href="https://fonts.googleapis.com/css2?family=Montserrat:wght@400;600&display=swap" rel="stylesheet">
<style>
  :root{
    --bg:#e9e7e4;
    --black:#121212;
    --gold:#c9a23c;
    --gold-light:#e7cf7a;
    --gold-dark:#9c7a22;
    --paper:#ffffff;
    --line:#d8d2c2;
    --mist:#d7e4e1;
    --ink:#555;
  }
  *{box-sizing:border-box;margin:0;padding:0}
  html,body{width:1200px;height:346px;overflow:hidden;background:var(--bg);font-family:"Montserrat",sans-serif}
  .sheet{position:absolute;box-shadow:0 2px 6px rgba(0,0,0,.25)}
  .brand{display:flex;align-items:center;gap:5px;color:var(--gold);font-weight:600;letter-spacing:.08em;text-transform:uppercase;white-space:nowrap}
  .brand .mark{width:8px;height:8px;background:var(--gold);flex:none}
  .small{font-size:4.5px;line-height:1.5;color:var(--ink)}

  /* business cards */
  .card{left:19px;width:130px;height:88px;display:flex;flex-direction:column;justify-content:center;align-items:center}
  .card-back{top:19px;background:var(--black);align-items:flex-start;padding:10px}
  .card-back .brand{font-size:6px}
  .card-back .small{color:#bbb;margin-top:6px}
  .card-front{top:130px;background:var(--black)}
  .card-gold{top:232px;background:linear-gradient(135deg,var(--gold-dark),var(--gold-light),var(--gold-dark))}
  .card .brand.big{font-size:8px}
  .card-gold .brand{color:var(--black)}
  .card-gold .brand .mark{background:var(--black)}

  /* letterheads */
  .letter{top:19px;width:223px;height:305px;background:var(--paper)}
  .letter-a{left:166px}
  .letter-b{left:406px}
  .letter .head{height:30px;background:var(--black);display:flex;align-items:center;justify-content:space-between;padding:0 12px}
  .letter .brand{font-size:5.5px}
  .letter .head .small{color:#bbb;text-align:right;font-size:3.6px}
  .letter .frame{position:absolute;left:70px;top:100px;width:84px;height:112px;border:1px solid var(--line)}
  .letter .frame::after{content:"";position:absolute;left:30px;top:44px;width:22px;height:22px;border:1px solid var(--line)}
  .letter .foot{position:absolute;bottom:10px;left:0;right:0;text-align:center;font-size:3.6px;color:var(--ink)}

  /* compliment slips */
  .slip{left:638px;width:233px;height:96px;background:var(--paper)}
  .slip-a{top:65px}
  .slip-b{top:204px}
  .slip .head{height:28px;background:var(--black);display:flex;align-items:center;justify-content:flex-end;padding:0 12px}
  .slip .brand{font-size:5px}
  .slip .small{padding:6px 12px;font-size:3.8px}

  /* envelopes */
  .env{left:895px;width:288px;height:100px;overflow:hidden}
  .env svg{position:absolute;inset:0}
  .env .brand{position:absolute;left:50%;transform:translateX(-50%);top:10px;font-size:5px}
  .env-mist{top:48px;background:var(--mist)}
  .env-gold{top:156px;background:linear-gradient(135deg,var(--gold-dark),var(--gold-light),var(--gold-dark))}
  .env-gold .brand{color:var(--black)}
  .env-gold .brand .mark{background:var(--black)}
  .env-white{top:202px;background:var(--paper)}
  .env-white .addr{position:absolute;left:14px;top:14px}
</style>
</head>
<body>
  <!-- business cards -->
  <div class="sheet card card-back">
    <div class="brand"><span class="mark"></span>Glanzwerk Garage</div>
    <p class="small">Tyttebærstien 7 · 0871 Oslo<br>post@glanzwerkstatt-eksempel.no<br>www.glanzwerkstatt-eksempel.no</p>
  </div>
  <div class="sheet card card-front"><div class="brand big"><span class="mark"></span>Glanzwerk Garage</div></div>
  <div class="sheet card card-gold"><div class="brand big"><span class="mark"></span>Glanzwerk Garage</div></div>

  <!-- letterheads -->
  <div class="sheet letter letter-a">
    <div class="head">
      <div class="brand"><span class="mark"></span>Glanzwerk Garage</div>
      <p class="small">Tyttebærstien 7<br>0871 Oslo<br>post@glanzwerkstatt-eksempel.no</p>
    </div>
    <div class="frame"></div>
  </div>
  <div class="sheet letter letter-b">
    <div class="head">
      <div class="brand"><span class="mark"></span>Glanzwerk Garage</div>
      <p class="small">www.glanzwerkstatt-eksempel.no</p>
    </div>
    <div class="frame"></div>
    <p class="foot">Tyttebærstien 7 · 0871 Oslo · post@glanzwerkstatt-eksempel.no · www.glanzwerkstatt-eksempel.no</p>
  </div>

  <!-- compliment slips -->
  <div class="sheet slip slip-a">
    <div class="head"><div class="brand"><span class="mark"></span>Glanzwerk Garage</div></div>
    <p class="small">Tyttebærstien 7, 0871 Oslo</p>
  </div>
  <div class="sheet slip slip-b">
    <div class="head"><div class="brand"><span class="mark"></span>Glanzwerk Garage</div></div>
    <p class="small">post@glanzwerkstatt-eksempel.no</p>
  </div>

  <!-- envelopes -->
  <div class="sheet env env-mist">
    <svg viewBox="0 0 288 100" preserveAspectRatio="none"><polyline points="0,0 144,48 288,0" fill="none" stroke="#b9cbc7" stroke-width="1"/></svg>
    <div class="brand"><span class="mark"></span>Glanzwerk Garage</div>
  </div>
  <div class="sheet env env-gold">
    <svg viewBox="0 0 288 100" preserveAspectRatio="none"><polyline points="0,0 144,48 288,0" fill="none" stroke="#8a6a1c" stroke-width="1"/></svg>
    <div class="brand"><span class="mark"></span>Glanzwerk Garage</div>
  </div>
  <div class="sheet env env-white">
    <div class="addr">
      <div class="brand" style="font-size:4.5px"><span class="mark"></span>Glanzwerk Garage</div>
      <p class="small" style="font-size:3.6px;margin-top:3px">Tyttebærstien 7 · 0871 Oslo</p>
    </div>
  </div>
</body>
</html>
```